依頼詳細
『ルミナリス+』のアルミ袋デザインを依頼させて頂きます。

参考サイトがありますのでこのサイトにイメージを合わせて頂けたらと思います。
https://hanato-store.space/shopping/lp.php?p=lumivelle

参考画像も貼っておきます。
参考画像のように、まわりは縁取りをお願いします。
色のイメージは、白と参考サイトに使われている薄いピンクでお願いします。

参考画像のようにセンターにロゴを配置して、サブタイトルをその下にお願いします。

そしてその下に成分をお願いします。

記載項目
サブタイトル: 超濃縮プエラリア配合!
~プエラバストを手に入れたいアナタに~

商品名: ルミナリス+

プラセンタ、コラーゲン、ヒアルロン酸、プエラリア、ローヤルゼリー、

1袋90粒入り
希望イメージ
シンプル 複雑
単色 カラフル
暗い 明るい
日常 高級
遊び心 厳粛
未来的 伝統的
女性的 男性的
希望する色
ピンク、白系
納品ファイル
• イラストレーター形式 (.ai)
• フォトショップ形式 (.psd)
補足説明
■ 選んだ理由

弊社のイメージとぴったりのデザインを作って頂きありがとうございました。

■ 提案者全員のお礼・コメント

沢山のご応募ありがとうございました。
今後ともよろしくお願いします。

```html
<!DOCTYPE html>
<html lang="ja">
<head>
<meta charset="utf-8">
<title>ルミナリス+ パウチデザイン</title>
<link href="https://fonts.googleapis.com/css2?family=Shippori+Mincho:wght@400;600&display=swap" rel="stylesheet">
<style>
  :root {
    --paper: #ffffff;
    --blush: #f8e0e4;
    --blush-deep: #f2cdd4;
    --gold: #c6a06a;
    --gold-soft: #dcc39c;
    --rose: #e58aa2;
    --ink: #3b2a2c;
    --trim: #555555;
  }
  html, body {
    margin: 0;
    padding: 0;
    width: 893px;
    height: 1200px;
    overflow: hidden;
    background: var(--paper);
    font-family: "Shippori Mincho", serif;
  }
  .canvas {
    position: relative;
    width: 893px;
    height: 1200px;
  }
  .trim-marks {
    position: absolute;
    inset: 0;
  }
  .pouch-face {
    position: absolute;
    left: 155px;
    top: 90px;
    width: 583px;
    height: 1010px;
    background: var(--blush);
  }
  .inner-frame {
    position: absolute;
    inset: 22px;
    border: 2px solid var(--gold-soft);
  }
  .corner-ornament {
    position: absolute;
    width: 130px;
    height: 130px;
    background: radial-gradient(circle at 30% 30%, var(--gold-soft), rgba(220,195,156,0) 70%);
    opacity: .8;
  }
  .corner-ornament.top-left { left: 14px; top: 14px; }
  .corner-ornament.top-right { right: 14px; top: 14px; transform: scaleX(-1); }
  .corner-ornament.bottom-left { left: 14px; bottom: 14px; transform: scaleY(-1); }
  .corner-ornament.bottom-right { right: 14px; bottom: 14px; transform: scale(-1,-1); }
  .crown {
    position: absolute;
    left: 241px;
    top: 30px;
    width: 100px;
    height: 90px;
    border-radius: 12px;
    background: linear-gradient(180deg, #d9b77f, var(--gold));
    opacity: .85;
  }
  .title-flourish {
    position: absolute;
    left: 66px;
    top: 140px;
    width: 450px;
    height: 180px;
    border-radius: 50%;
    background: radial-gradient(ellipse at center, rgba(248,224,228,0) 45%, rgba(229,138,162,.35) 62%, rgba(248,224,228,0) 75%);
  }
  .product-name {
    position: absolute;
    left: 0;
    right: 0;
    top: 188px;
    margin: 0;
    text-align: center;
    font-size: 60px;
    font-weight: 400;
    color: var(--ink);
    letter-spacing: 2px;
  }
  .product-subtitle {
    position: absolute;
    left: 0;
    right: 0;
    top: 265px;
    margin: 0;
    text-align: center;
    font-size: 20px;
    color: var(--rose);
    letter-spacing: 1px;
  }
  .tagline {
    position: absolute;
    left: 0;
    right: 0;
    top: 345px;
    margin: 0;
    text-align: center;
    font-size: 27px;
    color: var(--ink);
  }
  .ingredients {
    position: absolute;
    left: 0;
    right: 0;
    top: 695px;
    text-align: center;
  }
  .ingredients-heading {
    margin: 0 0 18px;
    font-size: 18px;
    font-weight: 400;
    color: var(--ink);
  }
  .ingredient-row {
    display: flex;
    justify-content: center;
    gap: 14px;
    margin-bottom: 16px;
  }
  .ingredient {
    width: 132px;
    height: 44px;
    line-height: 44px;
    border-radius: 22px;
    background: var(--paper);
    color: var(--rose);
    font-size: 18px;
  }
  .contents-count {
    margin: 8px 0 0;
    font-size: 18px;
    color: var(--ink);
  }
</style>
</head>
<body>
<div class="canvas">
  <svg class="trim-marks" width="893" height="1200" viewBox="0 0 893 1200" aria-hidden="true">
    <g stroke="var(--trim)" stroke-width="1.2" fill="none">
      <path d="M155 30 V80 M140 30 V80 M100 90 H145 M100 75 H145"/>
      <path d="M738 30 V80 M753 30 V80 M748 90 H793 M748 75 H793"/>
      <path d="M155 1110 V1170 M140 1110 V1170 M100 1100 H145 M100 1115 H145"/>
      <path d="M738 1110 V1170 M753 1110 V1170 M748 1100 H793 M748 1115 H793"/>
    </g>
  </svg>

  <section class="pouch-face">
    <div class="inner-frame"></div>
    <div class="corner-ornament top-left" role="img" aria-label="金色の唐草コーナー装飾"></div>
    <div class="corner-ornament top-right" role="img" aria-label="金色の唐草コーナー装飾"></div>
    <div class="corner-ornament bottom-left" role="img" aria-label="金色の唐草コーナー装飾"></div>
    <div class="corner-ornament bottom-right" role="img" aria-label="金色の唐草コーナー装飾"></div>

    <div class="crown" role="img" aria-label="金色の王冠イラスト"></div>
    <div class="title-flourish" role="img" aria-label="商品名を囲むピンクの渦巻き装飾フレーム"></div>

    <h1 class="product-name">ルミナリス+</h1>
    <p class="product-subtitle">超濃縮プエラリア配合</p>
    <p class="tagline">~プエラバストを手に入れたいアナタに~</p>

    <div class="ingredients">
      <h2 class="ingredients-heading">主配合成分</h2>
      <div class="ingredient-row">
        <span class="ingredient">プラセンタ</span>
        <span class="ingredient">ヒアルロン酸</span>
        <span class="ingredient">ローヤルゼリー</span>
      </div>
      <div class="ingredient-row">
        <span class="ingredient">コラーゲン</span>
        <span class="ingredient">プエラリア</span>
      </div>
      <p class="contents-count">1袋 90粒入</p>
    </div>
  </section>
</div>
</body>
</html>
```